Startup FinTech / Behavioural Science company needs website redesign

We are a startup company interested in redesigning our website. We have most of our content created already (viewable at www.tallyfern.co), but are interested in an upgraded look and feel. We are happy to adjust content as well based on design input. We will move hosting from hostbirch to webmarlo or similar hosting service, so portability of files is important to us. Our team will have the ability to make minor tweaks/content adjustments, but would look to engage with someone for more-comprehensive enhancements in the future.
Updates

Project Deadline Extended
Reason: Other business needs prevented me from providing timely feedback. I will work on feedback over the next two days but wanted to give additional time for design submissions and revisions.

Target Market(s)

Financial advisors in the US and UK, as well as potential end-users of the tools and potential investors

Industry/Entity Type

Information Technology

Coding

Coded - Design and coding required

Number of Pages Required

1 page

Font styles to use
Sans Serif

Requirements
Must have
• - Lighter, cleaner look and feel. We believe our current website is too heavy and "angular."
• - improved iconography to convey behavioural finance concepts (e.g., herd mentality, and illusion of control)
• - links to social media sites
• - integration with our hostbirch personality profile (viewable now at https://deanmollow.formquill.com/to/qRtZbe. Note: we will change this URL to tallyfern.formquill.com... as a part of the design process)
Nice to have
• - ability for us to add a tab/link to a blog in the future.
• - design that allows us to add additional
• - ability for us to add additional pages (e.g., results from our personality profiles, pages to customize sharing on social media)
• - simple ability to enter an email address to add to our mailing list/request more info
• - mobile-responsive design
Should not have
• - Should not have items like office directions and maps, since we are a virtual team.
• - Contact information (e.g., phone number) should be lower down the page vs. at the top
• - comments boxes or lengthy web forms. A simple name/email address is sufficient.

```html
<!DOCTYPE html>
<html lang="en">
<head>
<meta charset="utf-8">
<title>Tallyfern</title>
<link href="https://fonts.googleapis.com/css2?family=Raleway:wght@300;400;600;700;800&family=Lato:wght@300;400;700&display=swap" rel="stylesheet">
<style>
:root{
  --purple:#7d1f98;
  --ink:#1b1b1b;
  --text:#555;
  --grey-band:#f2f2f2;
  --footer-bar:#2e2e2e;
  --white:#fff;
}
*{box-sizing:border-box;margin:0;padding:0}
html,body{width:1200px;height:3766px;overflow:hidden}
body{font-family:"Lato",Arial,sans-serif;color:var(--text);background:var(--white);position:relative}
h1,h2,h3,h4{font-family:"Raleway",Arial,sans-serif}
.accent{color:var(--purple)}

/* Hero */
.hero{position:relative;height:678px;overflow:hidden}
.hero-photo{position:absolute;inset:0;background:
  radial-gradient(ellipse 700px 420px at 20% 75%,rgba(90,80,72,.55) 0%,rgba(90,80,72,0) 70%),
  linear-gradient(180deg,#eef0f2 0%,#e4e7ea 40%,#c9ced4 72%,#aab0b7 100%)}
.topbar{position:absolute;left:0;top:0;width:100%;height:90px;display:flex;align-items:center;justify-content:space-between;padding:0 78px}
.brand{font-family:"Raleway",sans-serif;font-weight:700;font-size:46px;color:var(--ink);letter-spacing:-1px}
.nav{display:flex;gap:48px;font-family:"Raleway",sans-serif;font-size:15px;color:var(--ink);font-weight:600}
.nav .active{color:var(--purple)}
.hero-copy{position:absolute;left:620px;top:215px;width:560px}
.hero-copy h1{font-size:55px;font-weight:800;line-height:1.05;color:var(--ink);letter-spacing:-1px}
.hero-copy .help{font-family:"Raleway",sans-serif;font-weight:300;font-size:50px;color:var(--ink);margin-top:8px}
.hero-copy .help b{font-weight:400}
.hero-copy .advisor{font-family:"Raleway",sans-serif;font-weight:700;font-size:21px;color:var(--ink);margin-top:6px}
.hero-copy .advisor u{text-underline-offset:3px}
.btn{display:inline-block;background:var(--purple);color:var(--white);font-family:"Raleway",sans-serif;font-weight:700;border-radius:4px}
.hero-copy .btn{margin-top:22px;font-size:17px;padding:16px 34px}

/* Problem */
.problem{height:218px;text-align:center;padding-top:52px}
.section-title{font-size:46px;font-weight:800;color:var(--ink);letter-spacing:-.5px}
.problem p{width:860px;margin:16px auto 0;font-size:15px;line-height:1.6}
.why-band{height:271px;background:var(--grey-band);text-align:center;padding-top:46px}
.why-band p{width:860px;margin:0 auto 22px;font-size:15px;line-height:1.7}
.why-band h3{font-size:27px;font-weight:700;color:var(--ink);margin-top:10px}
.why-cards{position:absolute;left:78px;top:1167px;width:1044px;height:264px;display:flex;box-shadow:0 14px 18px -10px rgba(0,0,0,.35)}
.why-card{flex:1;display:flex;flex-direction:column;align-items:center;padding-top:46px;color:var(--white);text-align:center}
.why-card.dark{background:linear-gradient(180deg,#444 0%,#2b2b2b 100%)}
.why-card.purple{background:linear-gradient(180deg,#8e2fb0 0%,#6f1b8b 100%)}
.why-card.purple:nth-child(3){background:linear-gradient(180deg,#9b3bba 0%,#7a2096 100%)}
.why-icon{width:110px;height:110px;border-radius:50%;background:rgba(255,255,255,.88)}
.why-card h4{font-family:"Lato",sans-serif;font-weight:400;font-size:21px;margin-top:40px}
.why-card .dark-title{margin-top:26px}
.why-card small{font-size:15px;line-height:1.3;padding:6px 18px 0}

/* Solution */
.solution-intro{position:absolute;top:1484px;width:100%;text-align:center}
.solution-intro p{font-family:"Raleway",sans-serif;font-weight:700;font-size:21px;color:var(--ink)}
.solution-intro h2{margin-top:4px}
.solution-grid{position:absolute;top:1606px;left:0;width:1200px;height:804px;display:grid;grid-template-columns:600px 600px;grid-template-rows:402px 402px}
.tile{position:relative;display:flex;flex-direction:column;align-items:center;justify-content:center;color:var(--white);text-align:center;padding:40px 40px 0}
.tile.purple{background:linear-gradient(135deg,#8f33ad 0%,#6e1a8a 100%)}
.tile.dark{background:linear-gradient(135deg,#5a5a5a 0%,#2f2f2f 100%)}
.tile .ring{width:104px;height:104px;border:2px solid var(--white);border-radius:50%;display:flex;align-items:center;justify-content:center;margin-bottom:22px}
.tile h3{font-size:34px;font-weight:700;letter-spacing:.3px;white-space:nowrap}
.tile p{font-size:16px;margin-top:10px;line-height:1.4;max-width:520px}
.notch{position:absolute;width:0;height:0;border:28px solid transparent;z-index:2}
.notch.right{right:-56px;top:50%;margin-top:-28px;border-left-color:#7c2398}
.notch.down{left:50%;bottom:-56px;margin-left:-28px;border-top-color:#3a3a3a}
.notch.left{left:-56px;top:50%;margin-top:-28px;border-right-color:#7c2398}

/* Team */
.team{position:absolute;top:2410px;width:100%;height:384px;text-align:center;padding-top:50px}
.team-list{display:flex;justify-content:center;gap:40px;margin-top:30px;text-align:left}
.member{display:flex;gap:18px;width:330px}
.member-side{display:flex;flex-direction:column;align-items:center}
.portrait{width:150px;height:150px;border-radius:50%;background:linear-gradient(180deg,#c9c9c9,#8d8d8d);border:6px solid #eee;box-shadow:0 2px 6px rgba(0,0,0,.2)}
.social-dot{width:40px;height:40px;border-radius:50%;border:2px solid var(--purple);margin-top:14px}
.member h4{font-size:21px;font-weight:700;color:var(--ink);line-height:1.15;margin-top:4px}
.member .role{font-style:italic;color:var(--purple);font-size:16px;margin-top:10px;padding-bottom:4px;border-bottom:1px solid #ccc}
.member ul{list-style:none;margin-top:8px;font-size:14px;line-height:1.45;color:#444}
.member li::before{content:"•";margin-right:7px}

/* Take profile */
.take-profile{position:absolute;top:2794px;width:100%;height:364px;background:linear-gradient(135deg,#e3e3e3 0%,#f1f1f1 50%,#d6d6d6 100%);text-align:center;padding-top:66px}
.take-profile p{font-family:"Raleway",sans-serif;font-size:28px;color:#666;margin-top:8px}
.take-profile .btn{margin-top:22px;font-size:20px;padding:16px 34px;display:inline-flex;align-items:center;gap:14px}

/* Newsletter */
.newsletter{position:absolute;top:3158px;width:100%;height:281px;text-align:center;padding-top:48px}
.newsletter p{width:620px;margin:14px auto 0;font-size:16px;line-height:1.55}
.subscribe{display:flex;justify-content:center;gap:14px;margin-top:30px}
.subscribe .field{width:424px;height:52px;border:1px solid #ccc;border-radius:3px;text-align:left;padding:16px 22px;color:#999;font-size:14px}
.subscribe .btn{height:52px;padding:0 26px;display:flex;align-items:center;font-size:15px}

/* Footer */
.footer{position:absolute;top:3439px;width:100%;height:263px;background:var(--purple);color:var(--white);padding:38px 0 0 78px;display:flex}
.footer-brand{width:267px;display:flex;align-items:center;gap:14px;height:180px}
.footer-brand .mark{width:70px;height:70px;border-radius:50%;background:var(--white)}
.footer-brand span{font-family:"Raleway",sans-serif;font-weight:700;font-size:38px}
.footer-col h4{font-size:21px;font-weight:700;margin-bottom:18px}
.links{width:215px}
.links li{list-style:none;font-size:14px;line-height:1.55}
.blog{width:313px}
.post{display:flex;gap:12px;margin-bottom:18px}
.thumb{width:50px;height:50px;border-radius:50%;background:linear-gradient(#ddd,#999);flex:none}
.post p{font-size:14px;line-height:1.35}
.post small{display:block;font-size:12px;margin-top:4px;opacity:.85}
.contact li{list-style:none;display:flex;align-items:center;gap:12px;font-size:15px;font-weight:700;margin-bottom:12px}
.socials{display:flex;gap:14px;margin-top:8px}
.socials span{width:52px;height:52px;border-radius:50%;background:var(--white)}
.socials span:first-child{background:#1d1d1d}
.bottom-bar{position:absolute;top:3702px;width:100%;height:64px;background:var(--footer-bar);color:#ddd;font-size:14px;display:flex;align-items:center;justify-content:space-between;padding:0 78px}
</style>
</head>
<body>

<section class="hero">
  <div class="hero-photo" role="img" aria-label="Photo of a climber helping another climber up a rocky summit above mountains and clouds"></div>
  <header class="topbar">
    <div class="brand">tallyfern</div>
    <nav class="nav">
      <span class="active">The Problem</span><span>The Solution</span><span>Our Team</span><span>Take Profile</span><span>Contact</span>
    </nav>
  </header>
  <div class="hero-copy">
    <h1>Money Decisions<br>can Stress you Out</h1>
    <div class="help">tally<b>fern</b> can HELP</div>
    <div class="advisor">Are you a financial advisor? <u>click here</u></div>
    <span class="btn">Let's Start Now</span>
  </div>
</section>

<section class="problem">
  <h2 class="section-title">THE <span class="accent">PROBLEM</span></h2>
  <p>Money and financial issues are the leading causes of anxiety for most of us. This financial stress is among the leading causes of divorce, addiction, obesity and depression.</p>
</section>

<section class="why-band">
  <p>Ask anyone the key to good physical health, and you're likely to get a correct answer: don't overeat, choose healthy foods and exercise regularly. The path to good physical health is not a mystery, but we have a hard time following it.</p>
  <p>Good financial health works the same way. We generally know what to do – spend less than we earn, save for a rainy day, and make non-emotional investment decisions – but have a hard time doing it.</p>
  <h3>Why?</h3>
</section>

<div class="why-cards">
  <div class="why-card dark">
    <div class="why-icon" role="img" aria-label="Icon of a head with a clock"></div>
    <h4 class="dark-title">Short-term Thinking</h4>
    <small>The belief that you can make an impulsive choice today...&gt;&gt;</small>
  </div>
  <div class="why-card purple">
    <div class="why-icon" role="img" aria-label="Icon of a sheep for herd mentality"></div>
    <h4>Herd Mentality</h4>
  </div>
  <div class="why-card purple">
    <div class="why-icon" role="img" aria-label="Icon of a pair of dice"></div>
    <h4>Gambler's Fallacy</h4>
  </div>
  <div class="why-card purple">
    <div class="why-icon" role="img" aria-label="Icon of a game controller"></div>
    <h4>Illusion of Control</h4>
  </div>
</div>

<div class="solution-intro">
  <p>This is where Tallyfern comes in.</p>
  <h2 class="section-title">THE <span class="accent">SOLUTION</span></h2>
</div>

<section class="solution-grid">
  <div class="tile purple" role="img" aria-label="Purple-tinted photo of a laptop on a desk">
    <div class="ring"><svg width="48" height="52" viewBox="0 0 48 52" fill="none" stroke="#fff" stroke-width="3"><rect x="6" y="6" width="36" height="44" rx="3"/><rect x="16" y="2" width="16" height="8" rx="2"/><path d="M14 22h20M14 30h20M14 38h12"/></svg></div>
    <h3>TAKE THE PROFILE</h3>
    <p>Take the Tallyfern profile to learn more about your financial personality and tendencies</p>
    <span class="notch right"></span>
  </div>
  <div class="tile dark" role="img" aria-label="Dark-tinted photo of hands on a keyboard">
    <div class="ring"><svg width="52" height="52" viewBox="0 0 52 52" fill="none" stroke="#fff" stroke-width="3"><path d="M8 44l10-10M44 8L34 18"/><path d="M14 26l12 12 6-6-12-12z"/><path d="M22 18l12 12 6-6-12-12z"/><path d="M22 24l-4 4M28 30l-4 4"/></svg></div>
    <h3>CONNECT YOUR ACCOUNTS</h3>
    <p>Connect your financial accounts to see your opportunities to be a better saver and investor</p>
    <span class="notch down"></span>
  </div>
  <div class="tile dark" role="img" aria-label="Dark-tinted photo of a man working at a computer">
    <div class="ring"><svg width="52" height="52" viewBox="0 0 52 52" fill="none" stroke="#fff" stroke-width="3"><path d="M44 26a18 18 0 1 1-8-15" stroke-dasharray="6 4"/><path d="M16 26l8 8 16-18"/></svg></div>
    <h3>CHECK YOUR PROGRESS</h3>
    <p>Check your progress over time to stay on track</p>
  </div>
  <div class="tile purple" role="img" aria-label="Purple-tinted photo of a person reading">
    <div class="ring"><svg width="52" height="52" viewBox="0 0 52 52" fill="none" stroke="#fff" stroke-width="3"><path d="M8 30l28-16 4 8-28 16z"/><path d="M22 34l-8 14M24 34l8 14"/><circle cx="22" cy="33" r="2"/></svg></div>
    <h3>GAIN BETTER INSIGHT</h3>
    <p>Receive valuable coaching to learn how your personality affects your financial decision making</p>
    <span class="notch left"></span>
  </div>
</section>

<section class="team">
  <h2 class="section-title">OUR <span class="accent">TEAM</span></h2>
  <div class="team-list">
    <div class="member">
      <div class="member-side"><div class="portrait" role="img" aria-label="Portrait photo of Dean Mollow"></div><span class="social-dot"></span></div>
      <div>
        <h4>Dean<br>Mollow, CFA</h4>
        <div class="role">CEO</div>
        <ul><li>FinTech Veteran</li><li>Investment Portfolio Manager</li><li>Halloway School of Business</li><li>Brennick Institute</li></ul>
      </div>
    </div>
    <div class="member">
      <div class="member-side"><div class="portrait" role="img" aria-label="Portrait photo of Marcus Orrin"></div><span class="social-dot"></span></div>
      <div>
        <h4>Marcus<br>Orrin</h4>
        <div class="role">CTO</div>
        <ul><li>Technology Expert</li><li>Predictive Analytics Solution Architect</li><li>Westmere University</li><li>University of Kestrel Bay</li></ul>
      </div>
    </div>
    <div class="member">
      <div class="member-side"><div class="portrait" role="img" aria-label="Portrait photo of Theo Vantrell"></div><span class="social-dot"></span></div>
      <div>
        <h4>Theo<br>Vantrell, PhD</h4>
        <div class="role">Chief Data Scientist</div>
        <ul><li>Decision Analysis Guru</li><li>Statistical Modeling Solution Architect</li><li>Northvale University</li><li>Brennick Institute</li></ul>
      </div>
    </div>
  </div>
</section>

<section class="take-profile" role="img" aria-label="Faded photo of a desk with a monitor and a mouse">
  <h2 class="section-title">TAKE <span class="accent">PROFILE</span></h2>
  <p>Want to learn about your financial personality?</p>
  <span class="btn"><svg width="24" height="24" viewBox="0 0 24 24" fill="none" stroke="#fff" stroke-width="2.5"><circle cx="11" cy="11" r="8"/><path d="M11 7v4l3 2"/></svg>CLICK HERE</span>
</section>

<section class="newsletter">
  <h2 class="section-title" style="font-size:44px">NEWSLETTER <span class="accent">SUBSCRIPTION</span></h2>
  <p>Subscribe to our Newsletter and get Latest News &amp; Updates. Join Our amazing Workshops &amp; Training to know much more</p>
  <div class="subscribe"><div class="field">E-mail</div><span class="btn">SUBSCRIBE</span></div>
</section>

<footer class="footer">
  <div class="footer-brand"><span class="mark"></span><span>tallyfern</span></div>
  <div class="footer-col links">
    <h4>Useful Links</h4>
    <ul><li>Home</li><li>The Problem</li><li>The Solution</li><li>Our Team</li><li>Take Profile</li><li>Contact</li></ul>
  </div>
  <div class="footer-col blog">
    <h4>Latest From Blog</h4>
    <div class="post"><span class="thumb" role="img" aria-label="Blog author photo"></span><p>Lorem Ipsum is simply dummy text of the.<small>12th June, 2016</small></p></div>
    <div class="post"><span class="thumb" role="img" aria-label="Blog author photo"></span><p>Lorem Ipsum is simply dummy text of the.<small>12th June, 2016</small></p></div>
  </div>
  <div class="footer-col">
    <h4>Get In Touch With Us</h4>
    <ul class="contact">
      <li><svg width="18" height="18" viewBox="0 0 24 24" fill="#fff"><path d="M6.6 10.8a15 15 0 0 0 6.6 6.6l2.2-2.2a1 1 0 0 1 1-.25 11.4 11.4 0 0 0 3.6.6 1 1 0 0 1 1 1V20a1 1 0 0 1-1 1A17 17 0 0 1 3 4a1 1 0 0 1 1-1h3.5a1 1 0 0 1 1 1c0 1.25.2 2.45.6 3.6a1 1 0 0 1-.25 1z"/></svg>+1 555 014 2280</li>
      <li><svg width="18" height="18" viewBox="0 0 24 24" fill="#fff"><path d="M6.6 10.8a15 15 0 0 0 6.6 6.6l2.2-2.2a1 1 0 0 1 1-.25 11.4 11.4 0 0 0 3.6.6 1 1 0 0 1 1 1V20a1 1 0 0 1-1 1A17 17 0 0 1 3 4a1 1 0 0 1 1-1h3.5a1 1 0 0 1 1 1c0 1.25.2 2.45.6 3.6a1 1 0 0 1-.25 1z"/></svg>+44 7700 900 418</li>
      <li><svg width="18" height="18" viewBox="0 0 24 24" fill="none" stroke="#fff" stroke-width="2"><rect x="3" y="5" width="18" height="14" rx="1"/><path d="M3 6l9 7 9-7"/></svg>info@tallyfern.co</li>
    </ul>
    <div class="socials"><span></span><span></span><span></span></div>
  </div>
</footer>

<div class="bottom-bar"><span>© <b>TALLYFERN</b> – 2017. All Rights Reserved.</span><span>Privacy Policy</span></div>

</body>
</html>
```